Business card por a urban DJ, up scale audience target

Need a sober design, modern, conservative colors but i can consider some options, y play rnb, hip hop, EDM and top40.

Business card for contact and personal info, double sided, use logo attrached please; im 42 so i need a card acording to my age an target audience.

Target Market(s)

Adult people, up scale audience

Industry/Entity Type

Music Download

Contact Information for Business Card

Cel (318) 5024471963 www.kelvarodun.com

Requirements
Must have
• open mind
Nice to have
• open mind
Should not have
• DJ

```html
<!DOCTYPE html>
<html lang="en">
<head>
<meta charset="utf-8">
<title>Kelvaro Business Card</title>
<link href="https://fonts.googleapis.com/css2?family=PT+Serif:wght@400;700&display=swap" rel="stylesheet">
<style>
  :root {
    --backdrop: #6e7889;
    --card: #ffffff;
    --card-shade: #eeeff1;
    --ink: #1c1a1a;
    --rule: #9a9a9a;
  }
  html, body {
    margin: 0;
    padding: 0;
    width: 1200px;
    height: 960px;
    overflow: hidden;
    background: var(--backdrop);
  }
  .stage {
    width: 1200px;
    height: 960px;
    display: flex;
    align-items: center;
    justify-content: center;
  }
  .business-card {
    position: relative;
    width: 840px;
    height: 480px;
    background: linear-gradient(135deg, var(--card) 0%, var(--card-shade) 45%, var(--card) 70%, var(--card-shade) 100%);
    box-shadow: 0 6px 18px rgba(0, 0, 0, 0.25);
    font-family: "PT Serif", Georgia, serif;
    color: var(--ink);
  }
  .brand {
    position: absolute;
    top: 110px;
    left: 0;
    right: 0;
    display: flex;
    align-items: center;
    justify-content: center;
    gap: 22px;
  }
  .brand-square {
    width: 34px;
    height: 34px;
    background: var(--ink);
  }
  .brand-name {
    margin: 0;
    font-size: 92px;
    font-weight: 700;
    letter-spacing: 6px;
    line-height: 1;
  }
  .divider {
    position: absolute;
    top: 290px;
    left: 170px;
    right: 170px;
    height: 1px;
    background: linear-gradient(90deg, transparent, var(--rule) 20%, var(--rule) 80%, transparent);
  }
  .contact {
    position: absolute;
    top: 322px;
    left: 0;
    right: 0;
    text-align: center;
    font-size: 24px;
    line-height: 1.6;
    letter-spacing: 1px;
  }
  .contact p { margin: 0; }
</style>
</head>
<body>
  <main class="stage">
    <section class="business-card">
      <div class="brand">
        <span class="brand-square"></span>
        <h1 class="brand-name">KELVARO</h1>
      </div>
      <div class="divider"></div>
      <div class="contact">
        <p class="contact-phone">M. (318) 5024471963</p>
        <p class="contact-web">www.kelvarodun.com</p>
      </div>
    </section>
  </main>
</body>
</html>
```